website update

We need to redesign our current website to be more personalised and sophisticated. We are physiotherapy clinic based in sydney australia, offer a range of clinical service such as Physiotherapy, Massage, sports injuries rehabilitation, Women's health (incontinency etc), Pilates classes, back pain exercise program, acupuncture, Gait analysis.
our current website is www.bluegumrehab.com.au
an example of ideal website is http://corvellabodyworks.com/
homepage: with a revolving displaying attached photos which is linked to relevants page

```html
<!DOCTYPE html>
<html lang="en">
<head>
<meta charset="utf-8">
<title>Bluegum Rehab — Physiotherapy &amp; Sports Care</title>
<link href="https://fonts.googleapis.com/css2?family=Open+Sans:wght@400;600;700;800&family=Oswald:wght@400;500&display=swap" rel="stylesheet">
<style>
:root{
  --green:#8cc43f;
  --green-dark:#6fa52a;
  --ink:#333333;
  --muted:#7a7a7a;
  --page:#ececec;
  --white:#ffffff;
  --footer:#2b2b2b;
  --footer-deep:#222222;
  --footer-text:#9a9a9a;
  --line:#dddddd;
}
*{box-sizing:border-box;margin:0;padding:0}
html,body{width:716px;height:1200px;overflow:hidden}
body{background:var(--page);font-family:"Open Sans",Arial,sans-serif;color:var(--ink);font-size:8px;line-height:1.5;position:relative}
.wrap{width:560px;margin:0 auto;position:relative}
.site-header{height:70px;display:flex;align-items:center;justify-content:space-between}
.brand-name{font-weight:700;font-size:17px;color:var(--ink);letter-spacing:.2px}
.header-phone{display:flex;align-items:center;gap:6px;color:var(--green);font-weight:700;font-size:10px;letter-spacing:.5px;white-space:nowrap}
.main-nav{background:var(--green);height:26px;display:flex;align-items:center;justify-content:space-between;padding:0 8px 0 0}
.main-nav a{color:var(--white);text-decoration:none;font-size:6.6px;font-weight:600;text-transform:uppercase;white-space:nowrap}
.main-nav .active{background:var(--green-dark);padding:8px 9px}
.slider{position:relative;height:270px;background:var(--white);margin-top:8px;padding:8px}
.slide-photo{position:absolute;left:8px;top:8px;right:8px;bottom:8px;background:linear-gradient(100deg,#b5b5b5 0%,#cfcfcf 45%,#ececec 62%,#f4f4f4 100%)}
.slide-copy{position:absolute;right:30px;top:100px}
.slide-copy h1{font-family:"Oswald",sans-serif;font-weight:500;color:var(--green);font-size:27px;line-height:1.1}
.slide-copy p{font-family:"Oswald",sans-serif;color:#444;font-size:18px;margin-top:4px;text-align:right}
.slide-arrows{position:absolute;right:16px;bottom:14px;display:flex;gap:3px}
.slide-arrows span{width:14px;height:14px;background:#555;color:#fff;font-size:8px;display:flex;align-items:center;justify-content:center}
.content{background:var(--white);padding:12px 18px 16px}
.section-title{text-align:center;font-weight:800;font-size:14px;letter-spacing:.5px}
.section-title em{font-style:normal;color:var(--green)}
.title-rule{width:50px;height:2px;background:var(--green);margin:3px auto 8px}
.intro{text-align:center;font-size:6.3px;color:var(--muted);margin:0 60px 12px}
.services{display:grid;grid-template-columns:repeat(3,1fr);gap:14px 20px}
.service h3{display:flex;align-items:center;gap:7px;font-size:9.5px;font-weight:800;text-transform:uppercase;line-height:1.1;margin-bottom:6px;min-height:22px}
.service-icon{width:22px;height:22px;border-radius:3px;background:var(--green);flex:none}
.service p{color:var(--muted);font-size:6.3px}
.read-more{color:var(--green);font-weight:700;font-size:6.8px;margin-top:4px;display:block}
.columns{display:grid;grid-template-columns:140px 1fr 140px;gap:20px;margin-top:20px;border-top:1px solid var(--line);padding-top:12px}
.col-title{font-weight:800;font-size:11px;margin-bottom:6px;white-space:nowrap}
.col-title em{font-style:normal;color:var(--green)}
.ticks{list-style:none}
.ticks li{font-size:6.5px;color:var(--muted);padding:3px 0;border-bottom:1px dotted var(--line);display:flex;gap:5px;align-items:center}
.ticks li::before{content:"";width:4px;height:4px;background:var(--green);border-radius:50%}
.welcome-photo{height:88px;background:linear-gradient(135deg,#cfd6c9,#9fb08e);margin-bottom:6px}
.welcome p{font-size:6.5px;color:var(--muted)}
.more{display:block;margin-top:8px;color:var(--green);font-weight:700;font-size:6.8px;border-top:1px solid var(--line);padding-top:4px}
.cta{background:var(--green);margin-top:16px;padding:11px 16px;display:flex;justify-content:space-between;align-items:center;color:var(--white);gap:16px}
.cta h2{font-weight:800;font-size:12px;text-transform:uppercase}
.cta p{font-size:6.3px;max-width:360px}
.cta-btn{border:1px solid #fff;padding:6px 10px;font-size:7.5px;font-weight:600;white-space:nowrap}
.site-footer{position:absolute;left:0;top:962px;width:716px;height:238px;background:var(--footer);color:var(--footer-text)}
.footer-grid{width:560px;margin:0 auto;display:grid;grid-template-columns:1fr 1fr .8fr 1fr;gap:16px;padding-top:14px}
.footer-grid h4{color:#eee;font-size:8.5px;font-weight:600;margin-bottom:6px}
.footer-grid p,.footer-grid li{font-size:6.3px;list-style:none;line-height:1.7}
.tweet-time{color:var(--green)}
.social{display:flex;gap:4px;margin-bottom:8px}
.social span{width:14px;height:14px;background:#4a4a4a;border-radius:2px}
.field{height:14px;background:#3c3c3c;border:1px solid #4b4b4b;margin-top:4px;font-size:6px;padding:2px 4px;display:flex;justify-content:space-between;align-items:center}
.field b{background:var(--green);color:#fff;padding:0 4px;font-weight:600}
.copyright{position:absolute;bottom:0;width:100%;height:22px;background:var(--footer-deep);font-size:6.3px;display:flex;align-items:center;justify-content:center}
</style>
</head>
<body>
<div class="wrap">
  <header class="site-header">
    <div class="brand"><span class="brand-name">Bluegum Rehab</span></div>
    <div class="header-phone">
      <svg width="11" height="11" viewBox="0 0 24 24"><path fill="#8cc43f" d="M6.6 10.8a15 15 0 006.6 6.6l2.2-2.2a1 1 0 011-.25 11.4 11.4 0 003.6.57 1 1 0 011 1V20a1 1 0 01-1 1A17 17 0 013 4a1 1 0 011-1h3.5a1 1 0 011 1c0 1.25.2 2.45.57 3.57a1 1 0 01-.25 1z"/></svg>
      CALL US : (02) 5550-1846
    </div>
  </header>
  <nav class="main-nav">
    <a class="active">Home</a><a>About Us</a><a>Common Conditions</a><a>Treatments</a><a>Workplace Services</a><a>Women's Health</a><a>Clinic Information</a><a>Contact Us</a>
  </nav>
  <section class="slider">
    <div class="slide-photo" role="img" aria-label="Physiotherapist guiding a patient through a reformer pilates stretch"></div>
    <div class="slide-copy"><h1>Get Well Move Well</h1><p>Enjoy The Freedom Again</p></div>
    <div class="slide-arrows"><span>‹</span><span>›</span></div>
  </section>
  <main class="content">
    <h2 class="section-title">WHAT <em>WE DO?</em></h2>
    <div class="title-rule"></div>
    <p class="intro">At Bluegum Rehab we believe that effective treatment comes with accurate diagnosis. In the clinic we take the time to understand your condition and goals.</p>
    <div class="services">
      <article class="service"><h3><span class="service-icon"></span>Physiotherapy</h3><p>At Bluegum Rehab we believe effective treatment starts with an accurate diagnosis and care tailored to your condition.</p><span class="read-more">READ MORE ›</span></article>
      <article class="service"><h3><span class="service-icon"></span>Massage</h3><p>At Bluegum Rehab we believe effective treatment starts with an accurate diagnosis and care tailored to your condition.</p><span class="read-more">READ MORE ›</span></article>
      <article class="service"><h3><span class="service-icon"></span>Sports Injuries<br>Rehabilitation</h3><p>At Bluegum Rehab we believe effective treatment starts with an accurate diagnosis and care tailored to your condition.</p><span class="read-more">READ MORE ›</span></article>
      <article class="service"><h3><span class="service-icon"></span>Women's Health</h3><p>At Bluegum Rehab we believe effective treatment starts with an accurate diagnosis and care tailored to your condition.</p><span class="read-more">READ MORE ›</span></article>
      <article class="service"><h3><span class="service-icon"></span>Back Pain Exercise<br>Program</h3><p>At Bluegum Rehab we believe effective treatment starts with an accurate diagnosis and care tailored to your condition.</p><span class="read-more">READ MORE ›</span></article>
      <article class="service"><h3><span class="service-icon"></span>Acupuncture</h3><p>At Bluegum Rehab we believe effective treatment starts with an accurate diagnosis and care tailored to your condition.</p><span class="read-more">READ MORE ›</span></article>
    </div>
    <div class="columns">
      <section>
        <h3 class="col-title">WE <em>TREAT</em></h3>
        <ul class="ticks"><li>Back and low back pain</li><li>Neck pain and headaches</li><li>Sports injuries</li><li>Shoulder problems</li><li>Knee and ankle conditions</li><li>Postural pain</li><li>Arthritis</li></ul>
        <span class="more">MORE DETAILS ›</span>
      </section>
      <section class="welcome">
        <h3 class="col-title">WELCOME TO <em>BLUEGUM REHAB</em></h3>
        <div class="welcome-photo" role="img" aria-label="Therapist treating a patient in the clinic"></div>
        <p>At Bluegum Rehab we believe that effective treatment comes with accurate diagnosis. In the clinic we listen, assess and build a plan around you.</p>
        <span class="more">READ MORE ›</span>
      </section>
      <section>
        <h3 class="col-title">WE <em>OFFER</em></h3>
        <ul class="ticks"><li>Manual therapy</li><li>Acupuncture and dry needling</li><li>Remedial massage</li><li>Sports taping</li><li>Injury rehabilitation</li><li>Post-operative rehab</li><li>Pilates classes</li></ul>
        <span class="more">MORE DETAILS ›</span>
      </section>
    </div>
    <section class="cta">
      <div><h2>Make an Appointment</h2><p>At Bluegum Rehab we believe that effective treatment comes with accurate diagnosis. Book a time that suits you and start feeling better.</p></div>
      <span class="cta-btn">Request an Appointment</span>
    </section>
  </main>
</div>
<footer class="site-footer">
  <div class="footer-grid">
    <div><h4>Contact Us</h4><p>Shop 4, 12 Wattle Street,<br>Sydney NSW 2000<br>Ph: (02) 5550-1846<br>hello@bluegumrehab.com.au</p></div>
    <div><h4>Latest Tweets</h4><p>New pilates classes start this month, spots are limited.<br><span class="tweet-time">2 days ago</span><br>Tips for a healthy back at your desk.<br><span class="tweet-time">5 days ago</span></p></div>
    <div><h4>Customer Service</h4><ul><li>Contact Us</li><li>Sitemap</li><li>FAQ</li><li>Bookings</li><li>Fees</li></ul></div>
    <div><h4>Connect With Us</h4><div class="social"><span></span><span></span><span></span><span></span></div><h4>Get Newsletters</h4><div class="field">Your email<b>Go</b></div></div>
  </div>
  <div class="copyright">© Copyright 2013 Bluegum Rehab. All Rights Reserved</div>
</footer>
</body>
</html>
```